'The Willow Lantern Boutique' Ecommerce boutique (womens clothing) needs a business card design

Ecommerce boutique (womens clothing) needs a business card design, we need a business card that's fresh, innovative, clean design that matches our quality products and attracts quality suppliers as well as customers.
We aim to create a feel good shopping experience that goes past the point of sale.
Updates
Target Market(s)
Women 18-35, fashion forward, disposable income, unique.
Industry/Entity Type
Boutique
Font styles to use
Colors
Designer to choose colors to be used in the design.
Look and feel
Each slider illustrates characteristics of the customer's brand and the style your logo design should communicate.

```html
<!DOCTYPE html>
<html lang="en">
<head>
<meta charset="utf-8">
<title>The Willow Lantern Boutique – Business Card</title>
<link href="https://fonts.googleapis.com/css2?family=Questrial&display=swap" rel="stylesheet">
<style>
  :root {
    --backdrop: #3a3836;
    --card-white: #ffffff;
    --card-black: #0d0d0d;
    --pattern-mid: #2a2c2e;
    --pattern-dark: #101112;
    --ink: #111111;
    --paper-text: #ffffff;
    --muted-text: #d9d9d9;
  }
  * { margin: 0; padding: 0; box-sizing: border-box; }
  html, body { width: 1200px; height: 856px; overflow: hidden; }
  body {
    background: var(--backdrop);
    font-family: "Questrial", "Century Gothic", sans-serif;
    position: relative;
  }
  .card {
    position: absolute;
    width: 540px;
    height: 310px;
    border-radius: 30px;
    overflow: hidden;
  }
  /* Front */
  .card-front {
    left: 40px; top: 110px;
    background: var(--card-white);
    display: flex; align-items: center; justify-content: center;
  }
  .brand-name {
    color: var(--ink);
    text-align: center;
    text-transform: uppercase;
    letter-spacing: 0.3em;
    font-size: 30px;
    line-height: 1.5;
  }
  .brand-name .brand-line-small { display: block; font-size: 30px; }
  /* Back */
  .card-back {
    left: 620px; top: 436px;
    background: var(--card-black);
    color: var(--paper-text);
  }
  .pattern-fill {
    position: absolute; inset: 0;
    background: radial-gradient(ellipse at 65% 55%, var(--pattern-mid) 0%, var(--pattern-dark) 70%, var(--card-black) 100%);
  }
  .holder {
    position: absolute; left: 34px; top: 28px;
  }
  .holder-name { font-size: 19px; font-weight: 700; letter-spacing: 0.01em; }
  .holder-role { font-size: 17px; color: var(--muted-text); margin-top: 2px; }
  .brand-band {
    position: absolute; left: 0; right: 0; top: 96px;
    display: flex; align-items: center; height: 26px;
  }
  .band-bar { background: var(--card-white); height: 22px; }
  .band-bar-left { width: 34px; }
  .band-bar-right { flex: 1; margin-top: 60px; }
  .band-text {
    font-size: 19px; font-weight: 700; text-transform: uppercase;
    padding: 0 10px; white-space: nowrap;
  }
  .contact-list {
    position: absolute; right: 24px; bottom: 26px;
    list-style: none; text-align: right;
    font-size: 16px; line-height: 1.75;
  }
  .contact-list li { display: flex; align-items: center; justify-content: flex-end; gap: 10px; }
  .contact-list .phone { font-size: 19px; letter-spacing: 0.04em; }
  .contact-icon { width: 14px; height: 14px; flex: none; }
</style>
</head>
<body>
  <section class="card card-front" aria-label="Business card front">
    <h1 class="brand-name">
      <span class="brand-line-small">The Willow Lantern</span>
      Boutique
    </h1>
  </section>

  <section class="card card-back" aria-label="Business card back">
    <div class="pattern-fill" role="img" aria-label="Dark grey paisley pattern covering the card background"></div>

    <div class="holder">
      <p class="holder-name">Maren Ashby</p>
      <p class="holder-role">Founder</p>
    </div>

    <div class="brand-band">
      <span class="band-bar band-bar-left"></span>
      <span class="band-text">The Willow Lantern Boutique</span>
      <span class="band-bar band-bar-right"></span>
    </div>

    <ul class="contact-list">
      <li class="phone">0400 555 218
        <svg class="contact-icon" viewBox="0 0 14 14" aria-hidden="true"><rect x="3.5" y="0.8" width="7" height="12.4" rx="1.4" fill="none" stroke="#fff" stroke-width="1.2"/><line x1="6" y1="11" x2="8" y2="11" stroke="#fff" stroke-width="1.2"/></svg>
      </li>
      <li>maren@willowlanternboutique.com.au
        <svg class="contact-icon" viewBox="0 0 14 14" aria-hidden="true"><rect x="1" y="3" width="12" height="8.5" fill="none" stroke="#fff" stroke-width="1.2"/><polyline points="1,3 7,8 13,3" fill="none" stroke="#fff" stroke-width="1.2"/></svg>
      </li>
      <li>www.thewillowlanternboutique.com
        <svg class="contact-icon" viewBox="0 0 14 14" aria-hidden="true"><circle cx="7" cy="7" r="5.8" fill="none" stroke="#fff" stroke-width="1.2"/><ellipse cx="7" cy="7" rx="2.6" ry="5.8" fill="none" stroke="#fff" stroke-width="1"/><line x1="1.2" y1="7" x2="12.8" y2="7" stroke="#fff" stroke-width="1"/></svg>
      </li>
    </ul>
  </section>
</body>
</html>
```